Harbor Print Studio gallery website

I need a Website for a gallery with a shopify integration or maybe even better also compatible with squarespace.
the website should have following riders: Künstler, Veranstaltungen, Shop, About Us.
some nice examples for inspiration of the website architecture are:
https://www.tarnelgalerie.com/
https://www.mossline-gallery.com/de/
https://zinnbergalerie.de/
It should be easy for us to make adaptations and fill the website with new content.
Attached there is the CI an logo for the brand.
Art Collectors,
artgallery
3 page

```html
<!DOCTYPE html>
<html lang="en">
<head>
<meta charset="utf-8">
<title>Harbor Print Studio – Gallery</title>
<link rel="stylesheet" href="https://fonts.googleapis.com/css2?family=Marcellus&family=DM+Sans:wght@400;600&display=swap">
<style>
  :root {
    --brand-red: #c0272d;
    --button-red: #b0364a;
    --ink: #141414;
    --header-bg: #ffffff;
    --hero-light: #f4f4f3;
    --hero-mid: #e6e6e4;
    --hero-low: #dcdcda;
    --on-button: #ffffff;
  }
  * { box-sizing: border-box; margin: 0; padding: 0; }
  html, body {
    width: 1200px;
    height: 3098px;
    overflow: hidden;
    background: var(--header-bg);
  }
  .page { position: relative; width: 1200px; height: 3098px; }

  .site-header {
    position: absolute; top: 0; left: 0;
    width: 1200px; height: 376px;
    background: var(--header-bg);
  }
  .menu-toggle {
    position: absolute; left: 64px; top: 146px;
    width: 120px; height: 32px;
  }
  .menu-toggle span {
    position: absolute; left: 0; width: 120px; height: 8px;
    background: var(--brand-red);
  }
  .menu-toggle span:first-child { top: 0; }
  .menu-toggle span:last-child { top: 24px; }

  .brand {
    position: absolute; left: 0; top: 222px; width: 1200px;
    display: flex; justify-content: center;
  }
  .brand-name {
    font-family: "DM Sans", sans-serif;
    font-weight: 400;
    font-size: 40px;
    letter-spacing: 1px;
    color: var(--ink);
    text-transform: uppercase;
  }

  .cart-link { position: absolute; left: 1054px; top: 122px; width: 64px; height: 74px; }

  .hero {
    position: absolute; top: 376px; left: 0;
    width: 1200px; height: 2722px;
  }
  .hero-backdrop {
    position: absolute; inset: 0;
    background: linear-gradient(180deg, var(--hero-light) 0%, var(--hero-mid) 55%, var(--hero-low) 100%);
  }
  .hero-content {
    position: absolute; left: 0; top: 520px; width: 1200px;
    display: flex; flex-direction: column; align-items: center;
    text-align: center;
  }
  .hero-title {
    font-family: "Marcellus", serif;
    font-weight: 400;
    font-size: 138px;
    line-height: 145px;
    color: var(--ink);
    width: 1120px;
    letter-spacing: -2px;
  }
  .hero-lead {
    margin-top: 114px;
    font-family: "DM Sans", sans-serif;
    font-weight: 400;
    font-size: 62px;
    line-height: 88px;
    color: var(--ink);
    width: 980px;
  }
  .shop-button {
    position: absolute; left: 238px; top: 1930px;
    width: 784px; height: 190px;
    background: var(--button-red);
    display: flex; align-items: center;
    text-decoration: none;
  }
  .shop-label {
    position: absolute; left: 138px;
    font-family: "DM Sans", sans-serif;
    font-weight: 600;
    font-size: 64px;
    color: var(--on-button);
  }
  .shop-arrow { position: absolute; left: 476px; top: 75px; }
</style>
</head>
<body>
<div class="page">
  <header class="site-header">
    <div class="menu-toggle" aria-label="Menu"><span></span><span></span></div>
    <div class="brand">
      <span class="brand-name">Harbor Print Studio</span>
    </div>
    <a class="cart-link" href="#" aria-label="Cart">
      <svg width="64" height="74" viewBox="0 0 64 74" fill="none" stroke="#c0272d" stroke-width="7" stroke-linejoin="round">
        <path d="M19 24 V16 a13 13 0 0 1 26 0 V24"/>
        <path d="M6 24 H58 V64 a6 6 0 0 1 -6 6 H12 a6 6 0 0 1 -6 -6 Z"/>
        <circle cx="20" cy="34" r="2" fill="#c0272d"/>
        <circle cx="44" cy="34" r="2" fill="#c0272d"/>
      </svg>
    </a>
  </header>

  <section class="hero">
    <div class="hero-backdrop" role="img" aria-label="Bright white gallery interior with framed artworks on the walls"></div>
    <div class="hero-content">
      <h1 class="hero-title">Discover Fine Art Masterpieces at Harbor Print Studio Gallery</h1>
      <p class="hero-lead">Embark on a journey through timeless beauty and artistic excellence at Harbor Print Studio Gallery. Explore our curated collection of exquisite masterpieces.</p>
    </div>
    <a class="shop-button" href="#">
      <span class="shop-label">SHOP</span>
      <svg class="shop-arrow" width="176" height="40" viewBox="0 0 176 40" fill="none" stroke="#ffffff" stroke-width="4">
        <path d="M0 20 H172"/>
        <path d="M154 4 L172 20 L154 36"/>
      </svg>
    </a>
  </section>
</div>
</body>
</html>
```